Clothing Brand E-Commerce Website Design

We would like you to provide an ecommerce design template in layered PSD for our clothing/fashion brand website called "TrelWick".
We want the site to have a simple but sleek design similar to the following sites:
http://www.pivorane.com/
http://corvatelle.com/
http://www.dulvenor.com/
We want it to look stunning and blow the example sites out of the water. For color scheme, please use your imagination and try to impress us with your creativity.
We like teal and beige pink, with teal dominant.
Teal #7AFFFF / #46C6C6
Beige/pink #FF7B7C / #C74646
We want you to develop the design for 3 pages:
1) Home Page
Samples:
http://www.pivorane.com/
http://corvatelle.com/
http://www.dulvenor.com/
2) Products List Page (e.g., lists all "Dresses" when category is selected)
http://www.pivorane.com/shop/casual-dresses
http://www.dulvenor.com/index.php?main_page=index&cPath=3
http://corvatelle.com/modest-dresses.html
http://www.quillmarsh.com/Product/Category.aspx?br=q47&category=dress_maxi
3) Product Detail Page (e.g., individual product page with "Add to Cart")
http://www.pivorane.com/shop/dresses/lumen-fern-dress
http://corvatelle.com/modest-dresses/modest-dress-tova.html
http://www.dulvenor.com/index.php?main_page=product_info&cPath=3&products_id=297
Industry/Entity Type
Fashion

```html
<!DOCTYPE html>
<html lang="en">
<head>
<meta charset="utf-8">
<title>TrelWick — Home</title>
<link href="https://fonts.googleapis.com/css2?family=Lato:ital,wght@0,300;0,400;0,700;1,300;1,400&display=swap" rel="stylesheet">
<style>
:root{
  --teal:#46c6c6;
  --teal-dark:#2e9c9c;
  --teal-soft:#e3f7f7;
  --pink:#ff7b7c;
  --red:#e8484a;
  --ink:#333;
  --muted:#777;
  --line:#e6e6e6;
  --footer:#f8f8f8;
}
*{box-sizing:border-box;margin:0;padding:0}
html,body{width:823px;height:1200px;overflow:hidden;background:#fff}
body{position:relative;font-family:"Lato",sans-serif;color:var(--ink)}
.abs{position:absolute}
a{color:inherit;text-decoration:none}

/* header */
.social-top{left:92px;top:14px;display:flex;gap:18px}
.social-top span{width:11px;height:11px;border-radius:50%;background:#e2e2e2;display:block}
.brand{left:0;width:823px;top:17px;text-align:center;font-size:16px;font-weight:700;color:var(--teal);letter-spacing:.5px}
.greeting{left:600px;top:18px;font-size:8px;color:#555}
.greeting b{font-weight:700;color:#333}
.cart{left:712px;top:12px}
.badge{left:701px;top:3px;width:14px;height:14px;border-radius:50%;background:var(--red);color:#fff;font-size:7px;text-align:center;line-height:14px}
.search{left:581px;top:33px;width:152px;height:23px;border:1px solid #e4e4e4;background:#f6f6f6}
.search .ph{position:absolute;left:6px;top:6px;font-size:8px;color:#aaa}
.search .btn{position:absolute;right:0;top:0;width:24px;height:21px;border-left:1px solid #e4e4e4}
.nav{left:233px;top:67px;display:flex;align-items:center;font-size:9px;color:#555}
.nav a{padding:0 10px;line-height:19px}
.nav a.active{background:var(--teal);color:#fff;padding:0 8px;margin-right:1px}
.rail{left:89px;top:0}

/* hero */
.hero{left:89px;top:117px;width:644px;height:253px;background:radial-gradient(circle at 68% 40%,#f3e0d6 0 14%,transparent 30%),linear-gradient(90deg,#6fcdcd,#a9e4e2 55%,#7fd4d3)}
.hero-title{left:164px;top:200px;font-size:21px;color:#fff;letter-spacing:.5px}
.hero-sub{left:164px;top:229px;font-size:12px;color:#fff;letter-spacing:3.6px;font-weight:300}
.hero-btn{left:164px;top:262px;width:117px;height:28px;background:#fff;color:#2c6f6f;font-size:10.5px;letter-spacing:1px;text-align:center;line-height:28px}

/* section headings */
.section-title{left:0;width:823px;text-align:center;font-size:11.5px;color:var(--teal-dark);letter-spacing:.8px}
.section-title::before,.section-title::after{content:"";display:inline-block;width:95px;height:1px;background:var(--line);vertical-align:middle;margin:0 14px}

/* products */
.card{top:441px;width:134px;height:188px;border:2px solid #f0f0f0;background:#fff;text-align:center}
.card .photo{position:absolute;left:8px;top:7px;width:116px;height:117px}
.card .sale{position:absolute;left:-2px;top:14px;background:var(--red);color:#fff;font-size:7px;padding:3px 7px}
.card .name{position:absolute;left:0;right:0;top:129px;font-size:7px;letter-spacing:.4px;color:#555}
.card .price{position:absolute;left:0;right:0;top:141px;font-size:8.5px;font-weight:700}
.card .price sup{font-size:5px}
.card .buy{position:absolute;left:50%;transform:translateX(-50%);top:158px;background:var(--red);color:#fff;font-size:6.5px;padding:4px 6px;border-radius:2px;white-space:nowrap}
.brick{background:linear-gradient(135deg,#c9735c,#b35e48 60%,#c98a72)}
.wood{background:linear-gradient(135deg,#c9c3bd,#a49a90 60%,#d4cec8)}
.loft{background:linear-gradient(135deg,#d8d6d2,#8a7d72 60%,#bdb6ae)}

/* testimonials */
.say-title{left:90px;top:660px;font-size:13.5px;color:var(--teal-dark);letter-spacing:.3px}
.quote{left:90px;top:694px;width:302px;height:53px;background:var(--teal-soft);padding:10px 12px;font-size:8px;line-height:12px;color:#444}
.quote-tail{left:192px;top:747px}
.author{left:91px;top:757px;font-size:9.5px;color:#444}
.more{left:315px;top:769px;font-size:8px;color:var(--teal-dark);font-weight:700;letter-spacing:.3px}
.follow{left:96px;top:796px;font-size:8.5px;color:var(--teal-dark);font-weight:700;display:flex;align-items:center;gap:8px;letter-spacing:.3px}
.follow i{width:11px;height:11px;border-radius:50%;background:var(--teal);display:block}

/* newsletter */
.notify{left:424px;top:691px;font-size:12.5px;font-style:italic;font-weight:300;color:#555}
.email{left:428px;top:720px;width:219px;height:34px;border:1px solid #ddd;font-size:10px;font-style:italic;color:#bbb;padding:10px 14px;font-weight:300}
.go{left:652px;top:720px;width:69px;height:34px;background:var(--pink);color:#fff;font-size:13px;text-align:center;line-height:34px;font-weight:300}

/* brands */
.brands{left:140px;top:875px;width:540px;display:flex;justify-content:space-between;align-items:center}
.brands span{font-size:20px;font-weight:700;color:#222;letter-spacing:.5px}

/* footer */
.footer{left:0;top:946px;width:823px;height:254px;background:var(--footer)}
.f-head{top:976px;font-size:11.5px;color:#444;letter-spacing:.3px}
.f-text{font-size:7.5px;line-height:13.5px;color:#666}
.f-text b{color:#444}
.post-title{font-size:8.5px;font-weight:700;color:#444;letter-spacing:.2px}
.post-title.hot{color:var(--red)}
.post-body{font-size:7.5px;line-height:10.5px;color:#777;margin:4px 0 13px 2px;width:165px}
.links{font-size:7.5px;line-height:16.5px;color:#777}
.links .hot{color:var(--red)}
.f-social{left:143px;top:1120px;display:flex;gap:12px}
.f-social span{width:9px;height:9px;border-radius:50%;background:#4a5d80;display:block}
.base-line{left:143px;top:1166px;width:537px;height:1px;background:#ebebeb}
.copy{left:143px;top:1179px;font-size:7px;color:#888}
.cards{left:578px;top:1177px;display:flex;gap:10px}
.cards span{width:18px;height:11px;background:#c9c9c9;display:block;border-radius:1px}
</style>
</head>
<body>

<header>
  <div class="abs social-top" aria-label="Social links"><span></span><span></span><span></span></div>
  <div class="abs brand">TrelWick</div>
  <div class="abs greeting">Howdy Mira Tolen&nbsp; | &nbsp;<b>Logut</b></div>
  <svg class="abs cart" width="12" height="11" viewBox="0 0 12 11" aria-label="Cart"><path d="M0 1h2l2 6h6l1.5-4.5H3" fill="none" stroke="#999" stroke-width="1.3"/><circle cx="4.5" cy="9.5" r="1" fill="#999"/><circle cx="9.5" cy="9.5" r="1" fill="#999"/></svg>
  <div class="abs badge">3</div>
  <div class="abs search"><span class="ph">Search</span>
    <svg class="btn" viewBox="0 0 24 21"><circle cx="11" cy="9.5" r="3.5" fill="none" stroke="#999" stroke-width="1.3"/><path d="M13.5 12l3 3" stroke="#999" stroke-width="1.5"/></svg>
  </div>
  <nav class="abs nav">
    <a class="active">Home</a><a>Women</a><a>Men</a><a>Shop now</a><a>About</a><a>Blog</a><a>Support</a>
  </nav>
  <svg class="abs rail" width="823" height="110" viewBox="0 0 823 110">
    <line x1="90" y1="101.5" x2="733" y2="101.5" stroke="#f5a3a3" stroke-width="2"/>
    <g fill="#fff" stroke="#f5a3a3" stroke-width="1"><circle cx="338" cy="101.5" r="3"/><circle cx="371" cy="101.5" r="3"/><circle cx="399" cy="101.5" r="3"/><circle cx="426" cy="101.5" r="3"/><circle cx="460" cy="101.5" r="3"/></g>
  </svg>
</header>

<section>
  <div class="abs hero" role="img" aria-label="Model with long wavy hair in a pale pink lace dress against a soft teal backdrop"></div>
  <svg class="abs" style="left:108px;top:224px" width="16" height="30" viewBox="0 0 16 30"><path d="M14 1L2 15l12 14" fill="none" stroke="#fff" stroke-width="1.2" opacity=".8"/></svg>
  <svg class="abs" style="left:684px;top:224px" width="16" height="30" viewBox="0 0 16 30"><path d="M2 1l12 14L2 29" fill="none" stroke="#fff" stroke-width="1.2" opacity=".8"/></svg>
  <div class="abs hero-title">NEW SEASON ARRIVALS.</div>
  <div class="abs hero-sub">CHECK OUT ALL THE NEW TRENDS</div>
  <a class="abs hero-btn">SHOP NOW</a>
</section>

<section>
  <h2 class="abs section-title" style="top:401px;font-weight:400">LATEST PRODUCTS</h2>

  <article class="abs card" style="left:90px">
    <div class="photo brick" role="img" aria-label="Model in red top and yellow skirt by a brick wall"></div>
    <span class="sale">-86%</span>
    <div class="name">DOLORE EU NULLA PARIATUR.</div>
    <div class="price">$120<sup>.00</sup></div>
    <a class="buy">SHOP NOW</a>
  </article>
  <article class="abs card" style="left:261px">
    <div class="photo wood" role="img" aria-label="Model in teal cardigan and striped dress by weathered wood"></div>
    <div class="name">ENIM AD MINIM VENIAM.</div>
    <div class="price">$1000<sup>.00</sup></div>
    <a class="buy">SHOP NOW</a>
  </article>
  <article class="abs card" style="left:427px">
    <div class="photo loft" role="img" aria-label="Model in black top and patterned skirt seated on a suitcase"></div>
    <div class="name">EXCEPTEUR SINT CUPIDATAT.</div>
    <div class="price">$340<sup>.00</sup></div>
    <a class="buy">SHOP NOW</a>
  </article>
  <article class="abs card" style="left:599px">
    <div class="photo brick" role="img" aria-label="Model in red top and yellow skirt by a brick wall"></div>
    <span class="sale">-86%</span>
    <div class="name">DOLORE EU NULLA PARIATUR.</div>
    <div class="price">$120<sup>.00</sup></div>
    <a class="buy">SHOP NOW</a>
  </article>
</section>

<section>
  <h2 class="abs say-title" style="font-weight:400">What people are saying about us</h2>
  <blockquote class="abs quote">@ Lorem Ipsum is simply dummy text of the printing and typesetting industry. Lorem Ipsum has been the industry's standard dummy text ever since the 1500s, when an unknown printer took a galley of type a</blockquote>
  <svg class="abs quote-tail" width="30" height="22" viewBox="0 0 30 22"><path d="M0 0h30L2 22z" fill="var(--teal-soft)"/></svg>
  <div class="abs author">Neom@ Vennabright</div>
  <a class="abs more">Load more tweets</a>
  <a class="abs follow"><i></i>Follow us on Chirpline</a>

  <p class="abs notify">Get notified when new product arrived</p>
  <div class="abs email">enter your email...</div>
  <a class="abs go">GO</a>
</section>

<section>
  <h2 class="abs section-title" style="top:827px;font-weight:400">TOP BRANDS</h2>
  <div class="abs brands">
    <span>CORVANE</span><span>BRANTLO</span><span>VELQA</span><span>OSTRELLE</span><span>BRANTLO</span>
  </div>
</section>

<footer>
  <div class="abs footer"></div>

  <h3 class="abs f-head" style="left:143px;font-weight:400">Our Stores</h3>
  <div class="abs f-text" style="left:143px;top:1004px">0276 North Alder Avenue<br>Rivermoor, CA 15390<br><b>(555) 310-4827</b></div>
  <div class="abs f-text" style="left:143px;top:1060px">118 Hollin Crest Drive<br>Marrowby, VA 23907<br><b>(555) 642-0193</b></div>
  <div class="abs f-social"><span></span><span></span><span></span><span></span><span></span></div>

  <h3 class="abs f-head" style="left:327px;font-weight:400">Blog Posts</h3>
  <div class="abs" style="left:328px;top:1006px">
    <div class="post-title hot">Duis aute irure dolor in reprehenderit.</div>
    <div class="post-body">in voluptate velit esse cillum dolore eu fugiat nulla pariatur.</div>
    <div class="post-title">Ut enim ad minim veniam.</div>
    <div class="post-body">in voluptate velit esse cillum dolore eu fugiat nulla pariatur.</div>
    <div class="post-title">officia deserunt mollit consectetur.</div>
    <div class="post-body">in voluptate velit esse cillum dolore eu fugiat nulla pariatur.</div>
  </div>

  <h3 class="abs f-head" style="left:512px;font-weight:400">Support</h3>
  <ul class="abs links" style="left:512px;top:1003px;list-style:none">
    <li>Terms &amp; Conditions</li><li>FAQ</li><li>Payment</li><li>Refunds</li><li>Track Order</li><li>Services</li>
  </ul>
  <ul class="abs links" style="left:615px;top:1003px;list-style:none">
    <li>Services</li><li>Press</li><li>Blog</li><li class="hot">About Us</li><li>Contact Us</li>
  </ul>

  <div class="abs base-line"></div>
  <div class="abs copy">© 2014trelwick.com &nbsp;-&nbsp; All Rights Reserved</div>
  <div class="abs cards" aria-label="Accepted payment methods"><span></span><span></span><span></span><span></span></div>
</footer>

</body>
</html>
```